Stationary Design for Stunning new Logo

I need to envelopes, letterhead, business cards designed to compliment our new logo.

We are a 25 year old printing company going through a brand refresh. All items should have the design extended to both sides for full print ability.

Industry/Entity Type

Printing

Requirements
Must have
• It must utilize the new logo & colors PMS 300 & PMS 295.

```html
<!DOCTYPE html>
<html lang="en">
<head>
<meta charset="utf-8">
<title>Brightsheet Stationery</title>
<link rel="stylesheet" href="https://fonts.googleapis.com/css2?family=Open+Sans:wght@400;600;700;800&family=Open+Sans+Condensed:wght@700&display=swap">
<style>
  :root {
    --pms-295: #002f6c;
    --pms-300: #005eb8;
    --sky: #4f95d6;
    --paper: #ffffff;
    --backdrop: #e8eaed;
    --ink: #3b4350;
    --muted: #7d8694;
    --hairline: #d6dae0;
  }
  * { margin: 0; padding: 0; box-sizing: border-box; }
  html, body { width: 1200px; height: 795px; overflow: hidden; }
  body {
    background: var(--backdrop);
    font-family: "Open Sans", Arial, sans-serif;
    color: var(--ink);
    position: relative;
  }
  .sheet {
    position: absolute;
    background: var(--paper);
    box-shadow: 0 2px 10px rgba(0, 0, 0, 0.12);
    overflow: hidden;
  }
  .brand { display: flex; align-items: center; gap: 6px; }
  .brand-dot { border-radius: 50%; background: var(--pms-300); flex: none; }
  .brand-name {
    font-weight: 800;
    color: var(--pms-295);
    letter-spacing: 0.04em;
    line-height: 1;
    white-space: nowrap;
  }
  .brand-tagline {
    font-family: "Open Sans Condensed", "Arial Narrow", sans-serif;
    font-weight: 700;
    color: var(--pms-300);
    text-transform: uppercase;
    letter-spacing: 0.03em;
    white-space: nowrap;
  }

  /* Business cards */
  .card-front { left: 60px; top: 170px; width: 220px; height: 126px;
    display: flex; flex-direction: column; align-items: center; justify-content: center; gap: 6px; }
  .card-front .brand-dot { width: 16px; height: 16px; }
  .card-front .brand-name { font-size: 18px; }
  .card-front .brand-tagline { font-size: 6.5px; }
  .card-back { left: 60px; top: 312px; width: 220px; height: 126px;
    background: linear-gradient(135deg, var(--pms-300), var(--pms-295)); color: #fff; padding: 16px 18px; }
  .card-back .person { font-size: 11px; font-weight: 700; letter-spacing: 0.05em; }
  .card-back .role { font-size: 7px; opacity: 0.85; margin-bottom: 12px; }
  .card-back .contact { font-size: 7px; line-height: 1.6; list-style: none; }
  .card-back .contact li { display: flex; align-items: center; gap: 5px; }
  .icon { width: 8px; height: 8px; flex: none; }

  /* Letterhead */
  .letterhead { left: 310px; top: 36px; width: 292px; height: 414px; padding: 22px 24px; }
  .letterhead .brand-dot { width: 12px; height: 12px; }
  .letterhead .brand-name { font-size: 14px; }
  .letterhead .brand-tagline { font-size: 5.5px; margin: 3px 0 0 18px; }
  .letter-meta { display: flex; gap: 16px; margin-top: 24px; font-size: 5.5px; line-height: 1.6; color: var(--muted); }
  .letter-meta .refs { width: 72px; flex: none; }
  .letter-body { flex: 1; }
  .letter-body p { margin-bottom: 6px; color: var(--ink); }
  .signoff { margin-top: 14px; }
  .signer { font-size: 7px; font-weight: 700; color: var(--pms-295); margin-top: 22px; }
  .signer-role { font-size: 5.5px; color: var(--muted); }
  .letter-footer { position: absolute; left: 24px; right: 24px; bottom: 18px;
    border-top: 2px solid var(--pms-300); padding-top: 6px;
    display: flex; justify-content: space-between; font-size: 5.5px; line-height: 1.6; color: var(--pms-295); }
  .letter-footer .contact-block { text-align: right; }
  .letter-footer b { color: var(--pms-300); }
  .letter-edge { position: absolute; left: 0; bottom: 0; width: 6px; height: 120px; background: var(--sky); }

  /* Folder */
  .folder { left: 640px; top: 50px; width: 330px; height: 480px; }
  .folder-spine { position: absolute; left: 10px; top: 0; bottom: 0; width: 1px; background: var(--hairline); }
  .folder-head { position: absolute; right: 26px; top: 78px; display: flex; flex-direction: column; align-items: flex-end; gap: 6px; }
  .folder .brand-dot { width: 22px; height: 22px; }
  .folder .brand-name { font-size: 24px; }
  .folder .brand-tagline { font-size: 7px; }
  .folder-band { position: absolute; left: 0; right: 0; top: 136px; height: 230px;
    background: linear-gradient(160deg, var(--pms-300) 0%, #0a4f9e 50%, var(--pms-295) 100%); }
  .folder-rule { position: absolute; left: 0; right: 0; top: 370px; height: 3px; background: var(--pms-295); }
  .folder-address { position: absolute; right: 26px; bottom: 24px; text-align: right;
    font-size: 7px; line-height: 1.5; color: var(--pms-300); text-transform: uppercase; }
  .folder-address strong { color: var(--pms-295); font-size: 8px; }

  /* Envelope front */
  .envelope-front { left: 300px; top: 482px; width: 360px; height: 180px; padding: 20px 22px; }
  .envelope-front .brand-dot { width: 14px; height: 14px; }
  .envelope-front .brand-name { font-size: 17px; }
  .envelope-front .brand-tagline { font-size: 5.5px; margin: 3px 0 0 20px; }
  .envelope-front .base-stripe { position: absolute; left: 0; right: 0; bottom: 0; height: 4px; background: var(--pms-300); }

  /* Envelope back */
  .envelope-back { left: 700px; top: 560px; width: 420px; height: 200px; }
  .flap { position: absolute; left: 0; right: 0; top: 0; height: 86px;
    background: linear-gradient(160deg, var(--pms-300), var(--pms-295)); }
  .envelope-back .sender { position: absolute; left: 0; right: 0; top: 112px; text-align: center;
    font-size: 6.5px; line-height: 1.7; color: var(--pms-300); text-transform: uppercase; }
  .envelope-back .sender strong { color: var(--pms-295); font-size: 7.5px; }
  .envelope-back .sender b { color: var(--pms-295); }

  /* Brand lockup */
  .lockup { position: absolute; left: 40px; top: 702px; }
  .lockup .brand { gap: 10px; }
  .lockup .brand-dot { width: 34px; height: 34px; }
  .lockup .brand-name { font-size: 38px; }
  .lockup .brand-tagline { font-size: 14px; margin-top: 4px; }
</style>
</head>
<body>

  <section class="sheet card-front" aria-label="Business card front">
    <div class="brand"><span class="brand-dot"></span><span class="brand-name">BRIGHTSHEET</span></div>
    <div class="brand-tagline">Reliable Service • Sharp Results • Fair Prices</div>
  </section>

  <section class="sheet card-back" aria-label="Business card back">
    <div class="person">SAM ORTEGA</div>
    <div class="role">Account Manager</div>
    <ul class="contact">
      <li><svg class="icon" viewBox="0 0 10 10"><path d="M5 0.5a3.3 3.3 0 0 0-3.3 3.3C1.7 6.3 5 9.5 5 9.5s3.3-3.2 3.3-5.7A3.3 3.3 0 0 0 5 0.5z" fill="#fff"/></svg>Harbor Lane Unit 48, Easton, NY 14802</li>
      <li><svg class="icon" viewBox="0 0 10 10"><path d="M2 1l2 2-1 1.2c.6 1.3 1.5 2.2 2.8 2.8L7 6l2 2-1.3 1.3C4.5 9 1 5.5.7 2.3z" fill="#fff"/></svg>123 555 0190</li>
      <li><svg class="icon" viewBox="0 0 10 10"><rect x="0.5" y="2" width="9" height="6" fill="none" stroke="#fff"/><path d="M.5 2L5 5.5 9.5 2" fill="none" stroke="#fff"/></svg>info@brightsheet.com</li>
      <li><svg class="icon" viewBox="0 0 10 10"><circle cx="5" cy="5" r="4.3" fill="none" stroke="#fff"/><path d="M.7 5h8.6M5 .7c-2 2.5-2 6.1 0 8.6M5 .7c2 2.5 2 6.1 0 8.6" fill="none" stroke="#fff" stroke-width=".7"/></svg>www.brightsheet.com</li>
    </ul>
  </section>

  <section class="sheet letterhead" aria-label="Letterhead">
    <div class="brand"><span class="brand-dot"></span><span class="brand-name">BRIGHTSHEET</span></div>
    <div class="brand-tagline">Reliable Service • Sharp Results • Fair Prices</div>
    <div class="letter-meta">
      <div class="refs">
        <div>Date: May 12, 2024</div>
        <div>Reference: BS-2041</div>
        <div>Subject: Print order</div>
      </div>
      <div class="letter-body">
        <p>Dear Ms. Clark,</p>
        <p>Thank you for choosing us for your new label run. Our team has reviewed the artwork and prepared a proof for your approval.</p>
        <p>Production can begin within two days of sign off, and delivery will follow the schedule agreed in our last call.</p>
        <p>Please contact me with any questions.</p>
        <p class="signoff">Sincerely,</p>
        <div class="signer">ALEX ROWAN</div>
        <div class="signer-role">Sales Director</div>
      </div>
    </div>
    <div class="letter-footer">
      <div><b>BRIGHTSHEET</b><br>Harbor Lane Unit 48<br>Easton, NY 14802</div>
      <div class="contact-block">123 555 0190<br>info@brightsheet.com<br>www.brightsheet.com</div>
    </div>
    <div class="letter-edge"></div>
  </section>

  <section class="sheet folder" aria-label="Presentation folder">
    <div class="folder-spine"></div>
    <div class="folder-head">
      <div class="brand"><span class="brand-dot"></span><span class="brand-name">BRIGHTSHEET</span></div>
      <div class="brand-tagline">Reliable Service • Sharp Results • Fair Prices</div>
    </div>
    <div class="folder-band" role="img" aria-label="Blue band with repeating arc pattern"></div>
    <div class="folder-rule"></div>
    <div class="folder-address">
      <strong>BRIGHTSHEET</strong><br>Harbor Lane Unit 48<br>Easton, NY 14802<br>United States
    </div>
  </section>

  <section class="sheet envelope-front" aria-label="Envelope front">
    <div class="brand"><span class="brand-dot"></span><span class="brand-name">BRIGHTSHEET</span></div>
    <div class="brand-tagline">Reliable Service • Sharp Results • Fair Prices</div>
    <div class="base-stripe"></div>
  </section>

  <section class="sheet envelope-back" aria-label="Envelope back">
    <div class="flap" role="img" aria-label="Envelope flap with blue repeating arc pattern"></div>
    <div class="sender">
      <strong>BRIGHTSHEET</strong><br>
      Harbor Lane Unit 48, Easton, NY 14802, United States<br>
      <b>P.</b> 123 555 0190 | <b>E.</b> info@brightsheet.com | <b>W.</b> www.brightsheet.com
    </div>
  </section>

  <div class="lockup">
    <div class="brand"><span class="brand-dot"></span><span class="brand-name">BRIGHTSHEET</span></div>
    <div class="brand-tagline">Reliable Service • Sharp Results • Fair Prices.</div>
  </div>

</body>
</html>
```